Vacation Rental business needs a prospective client flyer

We are a short-term vacation rental company in Steamboat Springs, Colorado called "Tidy Maple Cabins". We are looking to find new clients in the area by handing out flyers to the local Realtors to recommend using us to their clients.

We would like to touch on our low management fee of 18% and are local hands on approach.

Logo sheet is included for color and logo use.

```html
<!DOCTYPE html>
<html lang="en">
<head>
<meta charset="utf-8">
<title>Tidy Maple Cabins – Flyer</title>
<link rel="stylesheet" href="https://fonts.googleapis.com/css2?family=Oswald:wght@700&family=Montserrat:wght@300;400;600;700&display=swap">
<style>
  :root {
    --stage: #e9e9ec;
    --teal-top: #1b6a8c;
    --teal-bottom: #127a94;
    --band-blue: #1f74ad;
    --band-grey: #5a5a5c;
    --title-ink: #dedcf2;
    --logo-ink: #cfe4ec;
    --tagline-ink: #a9cdd9;
    --url-ink: #e6e6ea;
    --badge-blue: #1d66b0;
    --badge-ring: #b9bcc4;
    --badge-gold: #f2c53d;
    --wood-dark: #4a2612;
    --wood-mid: #8a4a22;
    --wood-light: #b8733c;
    --window-light: #c9d6cf;
    --forest: #3d5a3a;
    --plaid: #6b5660;
  }
  * { box-sizing: border-box; margin: 0; padding: 0; }
  html, body { width: 1200px; height: 800px; overflow: hidden; }
  body { background: var(--stage); position: relative; }

  .flyer {
    position: absolute;
    left: 330px; top: 18px;
    width: 540px; height: 764px;
    overflow: hidden;
    box-shadow: 0 6px 24px rgba(0,0,0,.18);
    display: flex; flex-direction: column;
  }

  .flyer__header {
    height: 150px;
    background: linear-gradient(180deg, var(--teal-top), var(--teal-bottom));
    display: flex; flex-direction: column; align-items: center; justify-content: center;
    gap: 8px;
  }
  .brand {
    display: flex; align-items: center; gap: 10px;
  }
  .brand-dot {
    width: 10px; height: 10px; border-radius: 50%;
    background: var(--logo-ink);
  }
  .brand-name {
    font-family: "Montserrat", sans-serif;
    font-weight: 400;
    font-size: 32px;
    color: var(--logo-ink);
    letter-spacing: 0.5px;
  }
  .brand-tagline {
    font-family: "Montserrat", sans-serif;
    font-weight: 300;
    font-size: 16px;
    letter-spacing: 6px;
    color: var(--tagline-ink);
    text-transform: lowercase;
  }

  .flyer__photo {
    position: relative;
    height: 404px;
    background:
      radial-gradient(ellipse 22% 30% at 12% 62%, rgba(61,90,58,.85), transparent 100%),
      radial-gradient(ellipse 30% 26% at 62% 22%, rgba(201,214,207,.75), transparent 100%),
      linear-gradient(90deg, transparent 24%, rgba(107,86,96,.45) 30%, transparent 36%, transparent 74%, rgba(107,86,96,.45) 80%, transparent 86%),
      radial-gradient(ellipse 40% 30% at 55% 70%, rgba(150,80,40,.6), transparent 100%),
      linear-gradient(165deg, var(--wood-light) 0%, var(--wood-mid) 50%, var(--wood-dark) 100%);
  }

  .fee-badge {
    position: absolute;
    right: 26px; bottom: 18px;
    width: 132px; height: 132px;
  }
  .fee-badge text { font-family: "Montserrat", sans-serif; }

  .flyer__title-band {
    height: 98px;
    background: var(--band-blue);
    display: flex; align-items: center; justify-content: center;
  }
  .flyer__title {
    font-family: "Oswald", sans-serif;
    font-weight: 700;
    font-size: 56px;
    letter-spacing: 2px;
    color: var(--title-ink);
    text-transform: uppercase;
    white-space: nowrap;
  }

  .flyer__footer {
    flex: 1;
    background: var(--band-grey);
    display: flex; align-items: center; justify-content: center;
  }
  .flyer__url {
    font-family: "Montserrat", sans-serif;
    font-weight: 400;
    font-size: 20px;
    letter-spacing: 3px;
    color: var(--url-ink);
  }
</style>
</head>
<body>
  <main class="flyer">
    <header class="flyer__header">
      <div class="brand">
        <span class="brand-dot"></span>
        <span class="brand-name">Tidy Maple Cabins</span>
      </div>
      <p class="brand-tagline">steamboat springs, co</p>
    </header>

    <section class="flyer__photo" role="img" aria-label="Photo of a couple relaxing on a leather sofa inside a cosy log cabin with tall windows, plaid curtains and pine trees outside">
      <svg class="fee-badge" viewBox="0 0 132 132" aria-label="Our low management fee of 18%">
        <circle cx="66" cy="66" r="64" fill="#8d929c"/>
        <circle cx="66" cy="66" r="60" fill="var(--badge-ring)"/>
        <circle cx="66" cy="66" r="52" fill="var(--badge-blue)"/>
        <circle cx="66" cy="66" r="47" fill="none" stroke="#e3e8f2" stroke-width="1" stroke-dasharray="3 2"/>
        <text x="66" y="46" text-anchor="middle" font-size="9.5" font-weight="600" fill="#fff">OUR LOW</text>
        <text x="66" y="58" text-anchor="middle" font-size="9.5" font-weight="600" fill="#fff">MANAGEMENT</text>
        <text x="66" y="70" text-anchor="middle" font-size="9.5" font-weight="600" fill="#fff">FEE OF</text>
        <text x="66" y="93" text-anchor="middle" font-size="22" font-weight="700" fill="var(--badge-gold)">18%</text>
      </svg>
    </section>

    <section class="flyer__title-band">
      <h1 class="flyer__title">Tidy Maple Cabins</h1>
    </section>

    <footer class="flyer__footer">
      <p class="flyer__url">www.tidymaplecabins.com</p>
    </footer>
  </main>
</body>
</html>
```